Consulting Group Website Landing Page Design

We are working with a Consulting Group in California. They provide consulting services to law enforcement agencies throughout the US.
Some sites to use for content:
https://www.wardmerecollegium.org
https://www.kfarrelteam.com
https://www.48qzadvisory.com
https://www.vlx.org
http://www.thorvikteam.com
Thank you for taking the time to consider designing a website for us. We are web developers based in Stockton, CA, USA. Most of our projects go through the same process. Understanding this process may help you win a project with us. We custom-code all of our websites in-house. We don’t have any requirements as to what tools you use for your design, but we ask that you follow these guidelines. Plus, please send your designs in at least 1200px. wide so they do not pixelate when we show the client.
IMAGES:
If you use any images or icons in the design, we ask that you have a link to the asset so we can purchase the image/icon. Most of the designs we submit do not have the customer’s images on them unless they have some great images. Be creative; show us the feeling you are trying to portray with your image choices. Use any royalty-free site you choose. We subscribe to Quillet and mainly use their images, but we can purchase images outside of Quillet. PLEASE NOTE: we will not submit designs to clients with watermarks on the images.
FONTS:
We ask that you identify the fonts you’re using in the design. This can be done in a message if you want. We typically use Brivo Fonts and Quillet Fonts.
CONTENT:
We're always open to different content and ideas. We often submit designs with stock images so the client can see our vision. We typically take pictures after the website launch to use their images with our vision. Lorem Ipsum is fine for paragraphs, but we ask that you make the Headers with correct English. We want to be able to show the vision and identify the sections of the website.
INSPIRATION:
We typically add a couple of links in the brief of websites we like to help you get started in your design.
REVISIONS:
We do not often ask for revisions of the designs unless we see something in the design that may not appeal to the client. If there are slight changes that we want to make, we do that in the development process.
FEEDBACK:
We rarely give feedback on designs during the design process. We are working on many website projects and do not have the time to provide feedback. We usually respond if your request is well thought out and asks specific questions, but a note asking “feedback, please” usually goes unanswered.
Number of Pages Required
1 page
Look and feel
Each slider illustrates characteristics of the customer's brand and the style your logo design should communicate.

```html
<!DOCTYPE html>
<html lang="en">
<head>
<meta charset="utf-8">
<title>Tidemark Consulting</title>
<link href="https://fonts.googleapis.com/css2?family=Poppins:ital,wght@0,400;0,500;0,600;1,400&display=swap" rel="stylesheet">
<style>
:root{
  --blue:#0d4b8c;
  --navy:#0a3a7a;
  --green:#7bbf2a;
  --ink:#333a44;
  --pale:#eef3fa;
  --field:#e6e9ee;
  --star:#c9a24a;
}
*{margin:0;padding:0;box-sizing:border-box}
html,body{width:1200px;height:3218px;overflow:hidden;background:#fff}
body{position:relative;font-family:'Poppins',sans-serif;color:var(--ink)}
.abs{position:absolute}
.btn{position:absolute;display:flex;align-items:center;justify-content:center;color:#fff;font-weight:600;font-size:15px;text-transform:uppercase;background:var(--navy)}
/* header */
.site-header{position:absolute;left:0;top:0;width:1200px;height:96px;background:#fff}
.brand{position:absolute;display:flex;align-items:center;gap:10px;font-weight:600;font-size:26px;color:var(--blue)}
.brand .dot{width:42px;height:42px;border-radius:50%;background:var(--blue)}
.nav{position:absolute;top:32px;left:598px;display:flex;gap:29px;font-size:16px}
.nav a{color:#222;text-decoration:none}
.nav a.active{color:var(--green);font-weight:500}
/* hero */
.hero{position:absolute;left:0;top:96px;width:1200px;height:600px}
.hero-text{position:absolute;left:115px;top:110px;color:#fff}
.hero-text .kicker{font-size:22px;letter-spacing:.5px}
.hero-text h1{font-size:33px;font-weight:600;margin-top:6px;letter-spacing:.5px}
.hero-text p{font-size:16px;line-height:29px;margin-top:22px;width:460px}
/* section titles */
.sec-title{position:absolute;left:0;width:1200px;text-align:center;font-size:37px;font-weight:600;color:var(--blue)}
.rule{position:absolute;height:3px;display:flex;gap:6px}
.rule i{display:block;height:3px;background:var(--green)}
/* about */
.about-title{position:absolute;left:111px;top:780px;font-size:37px;font-weight:600;color:var(--blue)}
.about-copy{position:absolute;left:111px;top:868px;width:532px;font-size:16px;line-height:30px;text-align:justify}
.about-copy p+p{margin-top:8px}
/* services */
.card{position:absolute;top:1427px;width:296px;height:377px;color:#fff;text-align:center}
.card.green{background:var(--green)}
.card.blue{background:var(--blue)}
.card .ring{position:absolute;left:87px;top:32px;width:122px;height:122px;border-radius:50%;background:rgba(255,255,255,.25);display:flex;align-items:center;justify-content:center}
.card .ring span{width:104px;height:104px;border-radius:50%;background:#fff;display:flex;align-items:center;justify-content:center}
.card h3{position:absolute;top:174px;width:100%;font-size:15px;font-weight:600}
.card p{position:absolute;top:210px;left:16px;right:16px;font-size:14px;line-height:25.5px}
.card a{position:absolute;top:314px;left:0;width:100%;color:#fff;font-size:14px;font-weight:500;text-decoration:underline}
/* testimonials */
.testimonials{position:absolute;left:0;top:1874px;width:1200px;height:491px;background:var(--pale)}
.quote{position:absolute;left:260px;top:204px;width:690px;text-align:center;font-style:italic;font-size:24.5px;line-height:39px;color:#2a2f38}
.stars{position:absolute;top:390px;left:0;width:1200px;text-align:center;color:var(--star);font-size:17px;letter-spacing:1px}
/* contact */
.field{position:absolute;border:1px solid var(--field);background:#fff;font-size:15px;color:#555;padding:15px 18px}
/* footer */
.site-footer{position:absolute;left:0;top:2891px;width:1200px;height:327px;background:var(--blue);color:#fff}
.site-footer .label{font-size:15px;font-weight:600;text-transform:uppercase}
.site-footer .val{font-size:16px;line-height:23px}
.vline{position:absolute;top:64px;width:1px;height:122px;background:rgba(255,255,255,.35)}
.social{position:absolute;width:42px;height:42px;border:2px solid #fff;border-radius:50%}
.copyright{position:absolute;top:280px;width:1200px;text-align:center;font-size:14px}
</style>
</head>
<body>

<header class="site-header">
  <div class="brand" style="left:111px;top:27px"><span class="dot"></span>Tidemark Consulting</div>
  <nav class="nav">
    <a class="active" href="#">Home</a><a href="#">About</a><a href="#">Services</a><a href="#">Contact</a>
  </nav>
  <div class="btn" style="left:949px;top:19px;width:140px;height:45px">Get a Quote</div>
</header>

<section class="hero">
  <svg class="abs" style="left:0;top:0" width="1200" height="600" viewBox="0 0 1200 600">
    <defs>
      <linearGradient id="heroFill" x1="0" y1="0" x2="1" y2="0">
        <stop offset="0" stop-color="#5d6f82"/>
        <stop offset=".45" stop-color="#2c3440"/>
        <stop offset=".75" stop-color="#3a4756"/>
        <stop offset="1" stop-color="#8aa0b4"/>
      </linearGradient>
    </defs>
    <polygon role="img" aria-label="Smiling police officer in uniform with arms crossed on a city street" points="0,0 1200,0 1200,437 600,545 0,437" fill="url(#heroFill)"/>
    <polygon points="290,497 600,588 908,497 600,560" fill="var(--green)"/>
    <polygon points="420,530 600,572 780,530 600,556" fill="var(--navy)"/>
  </svg>
  <div class="hero-text">
    <div class="kicker">WELCOME TO</div>
    <h1>TIDEMARK CONSULTING</h1>
    <p>Sed ut perspiciatis unde omnis iste natus erroroluptatem accusantium doloremque lorem ipsum lauda.</p>
  </div>
  <div class="btn" style="left:115px;top:292px;width:153px;height:48px">Learn More</div>
</section>

<h2 class="about-title">ABOUT US</h2>
<div class="rule" style="left:111px;top:830px"><i style="width:146px"></i><i style="width:34px"></i></div>
<div class="about-copy">
  <p>Neque porro quisquam est, qui dolorem ipsum quia dolor sit amet, consectetur, adipisci velit, sed quia non numquam eius modi tempo ra incidunt ut labore et dolore magnam aliquam quaerat voluptatem. Ut enim ad minima veniam.</p>
  <p>Qui dolorem ipsum quia dolor sit amet, consectetur, adipisci velit, sed quia non numquam eius modi tempo ra incidunt ut labore et dolore magnam aliquam quaerat voluptatem. Ut enim ad minima veniam.</p>
</div>
<div class="btn" style="left:111px;top:1117px;width:154px;height:48px">Learn More</div>
<div class="abs" style="left:747px;top:769px;width:341px;height:373px;border:2px solid var(--green)"></div>
<div class="abs" style="left:725px;top:792px;width:341px;height:373px;border:2px solid var(--blue)"></div>
<div class="abs" role="img" aria-label="Two police officers, a woman in front with arms crossed and a man behind" style="left:735px;top:780px;width:342px;height:373px;background:linear-gradient(135deg,#7d7f7d,#2d2f33 55%,#4a4c50);box-shadow:0 10px 20px rgba(0,0,0,.15)"></div>

<h2 class="sec-title" style="top:1294px">OUR SERVICES</h2>
<div class="rule" style="left:532px;top:1359px"><i style="width:74px"></i><i style="width:24px"></i></div>

<div class="card green" style="left:0">
  <div class="ring"><span><svg width="56" height="56" viewBox="0 0 56 56" fill="none" stroke="#333" stroke-width="2"><circle cx="28" cy="28" r="15"/><circle cx="28" cy="28" r="22" stroke-dasharray="6 5"/><path d="M21 28l5 5 9-10"/></svg></span></div>
  <h3>SYSTEMS ASSESSMENT</h3>
  <p>Lorem ipsum dolor sit amet, consecte tur adipiscilit, sed do eiusmod tempor incididunt ut labore et dolore magna</p>
  <a href="#">Read More</a>
</div>
<div class="card blue" style="left:302px">
  <div class="ring"><span><svg width="56" height="56" viewBox="0 0 56 56" fill="none" stroke="#333" stroke-width="2"><path d="M14 8h22l6 6v34H14z"/><path d="M19 20h16M19 26h16M19 32h10M19 38h8"/><path d="M38 32l7 3v6c0 4-3 6-7 8-4-2-7-4-7-8v-6z"/><path d="M35 41l2 2 4-4"/></svg></span></div>
  <h3>POLICY ANALYSIS</h3>
  <p>Lorem ipsum dolor sit amet, consecte tur adipiscilit, sed do eiusmod tempor incididunt ut labore et dolore magna</p>
  <a href="#">Read More</a>
</div>
<div class="card green" style="left:603px">
  <div class="ring"><span><svg width="56" height="56" viewBox="0 0 56 56" fill="none" stroke="#333" stroke-width="2"><path d="M30 10a18 18 0 1 0 0 36"/><circle cx="28" cy="28" r="8"/><path d="M34 18h12M36 28h12M34 38h12"/><circle cx="47" cy="18" r="2"/><circle cx="49" cy="28" r="2"/><circle cx="47" cy="38" r="2"/></svg></span></div>
  <h3>TECHNOLOGY SOLUTIONS</h3>
  <p>Lorem ipsum dolor sit amet, consecte tur adipiscilit, sed do eiusmod tempor incididunt ut labore et dolore magna</p>
  <a href="#">Read More</a>
</div>
<div class="card blue" style="left:904px">
  <div class="ring"><span><svg width="56" height="56" viewBox="0 0 56 56" fill="none" stroke="#333" stroke-width="2"><circle cx="28" cy="18" r="9" stroke-dasharray="4 3"/><circle cx="28" cy="18" r="4"/><circle cx="16" cy="32" r="4"/><circle cx="40" cy="32" r="4"/><circle cx="28" cy="30" r="4"/><path d="M8 48v-6a6 6 0 0 1 12 0v6M20 48v-6a8 8 0 0 1 16 0v6M36 48v-6a6 6 0 0 1 12 0v6M6 48h44"/></svg></span></div>
  <h3>MANAGEMENT CONSULTING</h3>
  <p>Lorem ipsum dolor sit amet, consecte tur adipiscilit, sed do eiusmod tempor incididunt ut labore et dolore magna</p>
  <a href="#">Read More</a>
</div>

<section class="testimonials">
  <h2 class="sec-title" style="top:76px">TESTIMONIALS</h2>
  <div class="rule" style="left:532px;top:141px"><i style="width:74px"></i><i style="width:24px"></i></div>
  <svg class="abs" style="left:36px;top:226px" width="34" height="34" viewBox="0 0 34 34" fill="none" stroke="#666" stroke-width="2"><circle cx="17" cy="17" r="15"/><path d="M24 17H10M15 12l-5 5 5 5"/></svg>
  <svg class="abs" style="left:1126px;top:226px" width="34" height="34" viewBox="0 0 34 34" fill="none" stroke="var(--blue)" stroke-width="2"><circle cx="17" cy="17" r="15"/><path d="M10 17h14M19 12l5 5-5 5"/></svg>
  <div class="abs" style="left:218px;top:192px;font-size:44px;color:#666;font-family:Georgia,serif;line-height:1">&ldquo;</div>
  <p class="quote">"Duis aute irure dolor in reprehenderit in voluptate velit esse cillum dolore eu fugiat nulla pariatur. Excepteur sint occaecat cupidatat non proident, sunt in culpa qui officia deserunt mollit anim id est laborum"</p>
  <div class="stars">★★★★★</div>
</section>

<h2 class="sec-title" style="top:2440px">CONTACT US</h2>
<div class="rule" style="left:525px;top:2504px"><i style="width:107px"></i><i style="width:24px"></i></div>
<div class="field" style="left:258px;top:2554px;width:335px;height:52px">First Name :</div>
<div class="field" style="left:603px;top:2554px;width:335px;height:52px">Last Name :</div>
<div class="field" style="left:258px;top:2616px;width:335px;height:52px">Email :</div>
<div class="field" style="left:603px;top:2616px;width:335px;height:52px">Phone :</div>
<div class="field" style="left:258px;top:2677px;width:680px;height:68px">Message :</div>
<div class="btn" style="left:509px;top:2764px;width:176px;height:53px;background:var(--green)">Submit Now</div>

<footer class="site-footer">
  <div class="brand" style="left:111px;top:84px;color:#fff;font-size:30px"><span class="dot" style="background:#fff;width:48px;height:48px"></span>Tidemark<br>Consulting</div>
  <div class="vline" style="left:440px"></div>
  <div class="vline" style="left:769px"></div>
  <svg class="abs" style="left:500px;top:80px" width="20" height="24" viewBox="0 0 20 24" fill="none" stroke="#fff" stroke-width="1.6"><path d="M10 23s8-8 8-14a8 8 0 0 0-16 0c0 6 8 14 8 14z"/><circle cx="10" cy="9" r="3"/></svg>
  <div class="abs" style="left:540px;top:75px"><div class="label">Address</div><div class="val">Tidemark Consulting<br>Address comes here</div></div>
  <div class="social" style="left:501px;top:149px"></div>
  <div class="social" style="left:554px;top:149px"></div>
  <svg class="abs" style="left:823px;top:80px" width="22" height="22" viewBox="0 0 22 22" fill="none" stroke="#fff" stroke-width="1.5"><path d="M4 2h4l2 5-3 2a12 12 0 0 0 6 6l2-3 5 2v4a2 2 0 0 1-2 2A18 18 0 0 1 2 4a2 2 0 0 1 2-2z"/></svg>
  <div class="abs" style="left:863px;top:74px"><div class="label">Phone</div><div class="val">+1 555-010-2040</div></div>
  <svg class="abs" style="left:825px;top:150px" width="22" height="16" viewBox="0 0 22 16" fill="none" stroke="#fff" stroke-width="1.5"><rect x="1" y="1" width="20" height="14"/><path d="M1 1l10 8 10-8"/></svg>
  <div class="abs" style="left:865px;top:144px"><div class="label">Email</div><div class="val">info@tidemarkconsulting.com</div></div>
  <div class="abs" style="left:111px;top:244px;width:978px;height:1px;background:rgba(255,255,255,.6)"></div>
  <div class="copyright">© 2023 Tidemark Consulting.All Rights Reserved.</div>
</footer>

</body>
</html>
```